Vitalquorra.com

I need a web design for a Online Wellness Center based in Chicago, IL and it's called "Vitalquorra" We provide Health risk assessment to individuals and interventions. Our portal has a Health Activity tracker where our members record health activities and aerobic miles and biometric data. Our Online wellness center tracks the participant's progress toward health goals and awards points for completed activities.
I started working on this website but the designer was not able to designer a website which describes what we do. I need a fresh look on this project. I need a very attractive, responsive website which says what we do.
These are the things we do.
1. We provide Health Risk Assessments to individuals and Co-operations
2. We Provide Free health screenings to undeserved communities
3. Assist individuals access free or affordable medications
4. We ask providers/doctors to see (or do a complete physical) one individual free of charge once a year (those individuals who are no insured and don't have money to pay from their pocket)
5. Assist patient access lab work at low cost
Our goal is to provide services that will lower the cost of care for our members.

Here is the website: www.vitalquorra.com still underdevelopment. PLEASE DO NOT COPY THIS STYLE OF WEBSITE. IT'S A BAD DESIGN AND THAT IS WHY I'M RE-DESIGNING THE SITE

Target Market(s)

Health individuals between the age of 21 to 65 Plus years old. Insured and uninsured

Industry/Entity Type

Health And Wellness

Coding

Coded - Design and coding required

Number of Pages Required

5+ page

Colors
0292cd

Requirements
Must have
• I'm still working on this websiteHere is the menu: Home, About us, Services, Health Screening, Providers, Contacts
• Please see. www.vitalquorra.com
Nice to have
• Event calender
• Upcoming Event
• Medication
• Lab assist
• Providers/Free Clinics

```html
<!DOCTYPE html>
<html lang="en">
<head>
<meta charset="utf-8">
<title>Vitalquorra – Online Wellness Center</title>
<link href="https://fonts.googleapis.com/css2?family=Open+Sans:wght@400;600;700&display=swap" rel="stylesheet">
<style>
:root{
  --blue:#0292cd;
  --blue-dark:#0a6fa3;
  --navy:#1d3f66;
  --dark:#262626;
  --darker:#1b1b1b;
  --text:#555;
  --light:#f1f1f1;
  --orange:#ee7d1f;
  --white:#fff;
}
*{box-sizing:border-box;margin:0;padding:0}
html,body{width:1200px;height:2392px;overflow:hidden}
body{font-family:"Open Sans",Arial,sans-serif;color:var(--text);background:var(--white);position:relative}
.wrap{width:740px;margin:0 auto;position:relative}

/* header */
.topbar{height:60px}
.topbar .wrap{height:60px;display:flex;align-items:center;justify-content:space-between;width:1080px}
.brand{display:flex;align-items:center;gap:10px;font-weight:700;font-size:26px;color:var(--navy)}
.brand i{width:26px;height:26px;border-radius:50%;background:var(--blue);display:block}
.account{display:flex;gap:6px;align-items:center}
.account input{width:90px;height:20px;border:1px solid #ccc;font-size:10px;padding:0 5px}
.account span{height:20px;padding:0 10px;font-size:10px;line-height:20px;color:#fff;background:var(--blue)}
.account span.alt{background:var(--dark)}

/* nav */
.mainnav{height:32px;background:var(--dark);position:relative;z-index:3}
.mainnav ul{list-style:none;display:flex;height:32px}
.mainnav li{position:relative;padding:0 22px;line-height:32px;font-size:12px;color:#fff}
.mainnav li.active{background:var(--blue)}
.dropdown{position:absolute;top:32px;left:0;width:128px;background:#fff;box-shadow:0 2px 6px rgba(0,0,0,.25)}
.dropdown div{font-size:10px;line-height:20px;padding:0 10px;color:#444;border-bottom:1px solid #eee}

/* hero */
.hero{height:488px;position:relative;background:linear-gradient(90deg,#dfe7ee 0%,#eef2f5 45%,#cfd9e1 100%)}
.hero-photo{position:absolute;inset:0}
.hero-panel{position:absolute;left:230px;top:0;width:220px;height:488px}
.tools{position:absolute;left:30px;top:70px;width:40px;background:var(--navy);padding:6px 0}
.tools div{width:28px;height:28px;margin:6px auto;border-radius:50%;background:var(--blue);display:flex;align-items:center;justify-content:center}
.tab{position:absolute;left:70px;top:70px;width:150px;height:26px;background:var(--blue);color:#fff;font-size:11px;line-height:26px;padding-left:10px;font-weight:600}
.finder{position:absolute;left:30px;top:350px;width:200px}
.finder h4{font-size:11px;color:var(--navy);font-weight:700;margin-bottom:8px}
.finder input{width:110px;height:20px;border:1px solid #aaa;font-size:9px;padding:0 5px;display:block;margin-bottom:10px}
.finder span{display:inline-block;background:var(--blue);color:#fff;font-size:11px;padding:6px 14px;font-weight:600}

/* about */
.about{text-align:center;padding-top:62px;height:328px}
h2.section{font-size:26px;font-weight:400;color:#333;margin-bottom:14px}
.about p{font-size:12px;line-height:17px;width:560px;margin:0 auto 18px}
.btn{display:inline-block;background:var(--blue);color:#fff;font-size:12px;padding:7px 20px}

/* services */
.services{text-align:center;height:402px;padding-top:12px}
.cards{display:flex;gap:20px;margin-top:18px}
.card{width:233px;height:260px;background:#f6f6f6;border:1px solid #e2e2e2;position:relative;padding-top:56px}
.card.on{background:var(--blue);color:#fff;border-color:var(--blue)}
.icon{position:absolute;top:-36px;left:50%;margin-left:-36px;width:72px;height:72px;border-radius:50%;background:#fff;border:3px solid var(--blue);display:flex;align-items:center;justify-content:center}
.icon i{width:54px;height:54px;border-radius:50%;background:var(--blue);display:flex;align-items:center;justify-content:center}
.card h3{font-size:14px;font-weight:600;margin-bottom:10px;color:#333}
.card.on h3{color:#fff}
.card p{font-size:11px;line-height:15px;padding:0 28px;margin-bottom:22px}
.card .btn{font-size:10px;padding:5px 14px}
.card.on .btn{background:var(--navy)}

/* banner */
.banner{height:280px;background:linear-gradient(180deg,#474747,#3a3a3a 60%,#505050);text-align:center;color:#fff;padding-top:80px}
.banner h2{font-size:30px;font-weight:400;line-height:38px;margin-bottom:20px}
.banner .btn{background:var(--orange);font-size:13px;padding:8px 22px}

/* news + schedule */
.updates{height:520px;background:var(--light);padding-top:24px}
.updates .wrap{display:flex;gap:30px}
.box{background:#fff;border:1px solid #ddd;width:355px;height:420px}
.box-head{height:34px;background:var(--blue);color:#fff;font-size:14px;line-height:34px;padding-left:16px;border-left:6px solid var(--navy);border-right:6px solid var(--navy)}
.news{display:flex;gap:12px;padding:20px 18px 6px}
.thumb{width:110px;height:80px;background:linear-gradient(135deg,#d8dde2,#aab7c2);flex:none}
.news h5{font-size:11px;color:var(--blue);margin-bottom:6px}
.news p{font-size:11px;line-height:15px}
.more{text-align:center;margin-top:26px}
.calendar{margin:20px auto 0;width:260px}
.cal-month{background:#e1e1e1;text-align:center;font-size:12px;font-weight:600;line-height:26px;color:#333}
.cal-grid{display:grid;grid-template-columns:repeat(7,1fr);gap:3px;background:#555;padding:6px}
.cal-grid span{height:30px;background:#6d6d6d;color:#fff;font-size:10px;display:flex;align-items:center;justify-content:center}
.cal-grid span.day{background:#444;height:18px}
.cal-grid span.on{background:var(--blue)}
.box .cta{text-align:center;margin-top:20px}
.box .cta .btn{font-size:10px;padding:6px 16px}

/* footer */
.footer{height:274px;background:var(--darker);color:#bbb;padding-top:36px;position:relative}
.footer .wrap{display:flex;justify-content:space-between;width:760px}
.col h6{color:#fff;font-size:13px;font-weight:600;margin-bottom:12px}
.col li{list-style:none;font-size:11px;line-height:22px;padding-left:12px;position:relative}
.col li::before{content:"";position:absolute;left:0;top:9px;width:4px;height:4px;background:var(--blue)}
.contact div{display:flex;gap:10px;font-size:11px;line-height:16px;margin-bottom:14px}
.contact i{width:22px;height:22px;border-radius:50%;background:var(--blue);flex:none}
.quick input{display:block;width:150px;height:20px;background:#333;border:1px solid #444;margin-bottom:6px}
.quick input.msg{height:40px}
.quick span{display:inline-block;background:var(--blue);color:#fff;font-size:10px;padding:4px 12px}
.copy{position:absolute;bottom:0;left:0;right:0;height:34px;border-top:1px solid #333;font-size:10px;line-height:34px;padding-left:40px;color:#888}
</style>
</head>
<body>

<header class="topbar">
  <div class="wrap">
    <div class="brand"><i></i>Vitalquorra</div>
    <div class="account"><input placeholder="Search"><span>Login</span><span class="alt">Sign Up</span></div>
  </div>
</header>

<nav class="mainnav">
  <div class="wrap">
    <ul>
      <li class="active">Home</li>
      <li>About Us</li>
      <li>Our Service</li>
      <li>Health Screening
        <div class="dropdown"><div>Screening Package</div><div>Screening Services</div><div>Events</div></div>
      </li>
      <li>Provider</li>
      <li>Contact</li>
    </ul>
  </div>
</nav>

<section class="hero">
  <div class="hero-photo" role="img" aria-label="Photo of a smiling lab technician working with test tubes in a bright clinic"></div>
  <div class="hero-panel">
    <div class="tools">
      <div><svg width="14" height="14" viewBox="0 0 14 14"><path d="M2 7l5-5 5 5v6H2z" fill="#fff"/></svg></div>
      <div><svg width="14" height="14" viewBox="0 0 14 14"><rect x="3" y="2" width="8" height="10" fill="none" stroke="#fff" stroke-width="1.5"/></svg></div>
      <div><svg width="14" height="14" viewBox="0 0 14 14"><path d="M6 2h2v4h4v2H8v4H6V8H2V6h4z" fill="#fff"/></svg></div>
      <div><svg width="14" height="14" viewBox="0 0 14 14"><circle cx="7" cy="7" r="5" fill="none" stroke="#fff" stroke-width="1.5"/><path d="M7 4v3h2" stroke="#fff" stroke-width="1.5" fill="none"/></svg></div>
      <div><svg width="14" height="14" viewBox="0 0 14 14"><circle cx="7" cy="4.5" r="2.5" fill="#fff"/><path d="M2 13c0-3 2-5 5-5s5 2 5 5z" fill="#fff"/></svg></div>
    </div>
    <div class="tab">Health Risk Assessments</div>
    <div class="finder">
      <h4>Free and Partial Clinics in Illinois</h4>
      <input placeholder="Enter your zip code">
      <span>SEARCH</span>
    </div>
  </div>
</section>

<section class="about">
  <h2 class="section">About Us</h2>
  <p>Lorem Ipsum is simply dummy text of the printing and typesetting industry. Lorem Ipsum has been the industry's standard dummy text ever since the 1500s, when an unknown printer took a galley of type and scrambled it to make a type specimen book. It has survived not only five centuries, but also the leap into electronic typesetting, remaining essentially unchanged. It was popularised.</p>
  <span class="btn">Read More</span>
</section>

<section class="services">
  <h2 class="section">Service</h2>
  <div class="wrap cards" style="margin-top:56px">
    <div class="card">
      <div class="icon"><i><svg width="26" height="26" viewBox="0 0 26 26"><path d="M10 3h6v7h7v6h-7v7h-6v-7H3v-6h7z" fill="#fff"/></svg></i></div>
      <h3>Emergency Care</h3>
      <p>Contrary to popular belief, Lorem Ipsum is not simply random text. It has roots in a piece.</p>
      <span class="btn">MORE</span>
    </div>
    <div class="card on">
      <div class="icon"><i><svg width="26" height="26" viewBox="0 0 26 26"><rect x="4" y="9" width="18" height="8" rx="4" fill="#fff" transform="rotate(-40 13 13)"/></svg></i></div>
      <h3>Medication</h3>
      <p>Contrary to popular belief, Lorem Ipsum is not simply random text. It has roots in a piece.</p>
      <span class="btn">MORE</span>
    </div>
    <div class="card">
      <div class="icon"><i><svg width="26" height="26" viewBox="0 0 26 26"><path d="M10 3h6v2h-1v6l6 11H5l6-11V5h-1z" fill="#fff"/></svg></i></div>
      <h3>Lab work at low cost</h3>
      <p>Contrary to popular belief, Lorem Ipsum is not simply random text. It has roots in a piece.</p>
      <span class="btn">MORE</span>
    </div>
  </div>
</section>

<section class="banner" role="img" aria-label="Dimmed photo of a doctor consulting with a patient">
  <h2>We Provide Free health screenings to<br>undeserved communities</h2>
  <span class="btn">Know More</span>
</section>

<section class="updates">
  <div class="wrap">
    <div class="box">
      <div class="box-head">Latest News</div>
      <div class="news">
        <div class="thumb" role="img" aria-label="News photo of a medical team"></div>
        <div><h5>02 Jan 2015 &nbsp; 5</h5><p>It is a long established fact that a reader will be distracted by the readable content of a page.</p></div>
      </div>
      <div class="news">
        <div class="thumb" role="img" aria-label="News photo of a health screening event"></div>
        <div><h5>02 Jan 2015 &nbsp; 5</h5><p>It is a long established fact that a reader will be distracted by the readable content of a page.</p></div>
      </div>
      <div class="more"><span class="btn" style="font-size:10px;padding:5px 14px">Read More</span></div>
    </div>
    <div class="box">
      <div class="box-head">Our Screening Schedule</div>
      <div class="calendar">
        <div class="cal-month">OCTOBER</div>
        <div class="cal-grid">
          <span class="day">S</span><span class="day">M</span><span class="day">T</span><span class="day">W</span><span class="day">T</span><span class="day">F</span><span class="day">S</span>
          <span></span><span></span><span></span><span>1</span><span>2</span><span>3</span><span>4</span>
          <span>5</span><span>6</span><span>7</span><span>8</span><span class="on">9</span><span>10</span><span>11</span>
          <span>12</span><span>13</span><span>14</span><span>15</span><span>16</span><span>17</span><span>18</span>
          <span>19</span><span>20</span><span class="on">21</span><span>22</span><span>23</span><span>24</span><span>25</span>
          <span>26</span><span>27</span><span>28</span><span>29</span><span>30</span><span>31</span><span></span>
        </div>
      </div>
      <div class="cta"><span class="btn">VIEW SCHEDULE</span></div>
    </div>
  </div>
</section>

<footer class="footer">
  <div class="wrap">
    <div class="col"><h6>Main menu</h6><ul><li>Home</li><li>About Us</li><li>Service</li><li>Blog</li><li>Contact</li></ul></div>
    <div class="col"><h6>Information</h6><ul><li>Partners</li><li>Legal Notice</li><li>Terms and conditions of use</li><li>Benefits of Donations</li><li>Referrals</li></ul></div>
    <div class="col contact"><h6>Contact us</h6>
      <div><i></i><span>Vitalquorra<br>2150 Larkmoor Avenue<br>Chicago IL 60614</span></div>
      <div><i></i><span>(312) 555-0184</span></div>
      <div><i></i><span>info@vitalquorra.com</span></div>
    </div>
    <div class="col quick"><h6>Quick Contact</h6><input><input><input class="msg"><span>Submit</span></div>
  </div>
  <div class="copy">Vitalquorra 2015. All Rights Reserved.</div>
</footer>

</body>
</html>
```